Customer Dashboard Design for Email Security SaaS

Mailbrook is a commercial email spam filter offered as a SaaS product, built and operated by a small German hosting provider. It protects business email accounts against spam, phishing, scam, and viruses using a multilayer filtering pipeline that combines traditional spam detection with AI-powered classification. The product runs entirely on German infrastructure, ensuring data sovereignty for European customers.

We need a complete redesign of the customer-facing dashboard. This is the web application where paying customers manage their email filtering: view their mail log, check quarantined emails, manage allow/blocklists, configure their settings, and handle their subscription. It is the primary touchpoint between Mailbrook and its customers.

Our customers are system administrators, IT managers at small-to-medium businesses, and operators of small hosting providers. They are technically competent but not designers. They expect professional, efficient tools that respect their time. They typically manage 10–500 email accounts and check the dashboard a few times per week, with heavier use during spam incidents.

We have attached the current mockups which really need to be replaced with something good looking.

Target Market(s)

System administrators, IT managers at small-to-medium businesses, and operators of small hosting providers.

Industry/Entity Type

SaaS

Number of Pages Required

5+ page

```html
<!DOCTYPE html>
<html lang="de">
<head>
<meta charset="utf-8">
<title>Mailbrook – Mail-Log</title>
<link href="https://fonts.googleapis.com/css2?family=Inter:wght@400;500;600&display=swap" rel="stylesheet">
<style>
:root{
  --bg:#f4f3ef;
  --surface:#ffffff;
  --row-alt:#faf8f4;
  --border:#ebe9e4;
  --text:#1c1f1d;
  --text-muted:#6b6f6c;
  --text-faint:#9a9d9a;
  --brand:#3b8a5d;
  --orange:#d98a2b;
  --orange-bg:#fdf1df;
  --red:#d0473f;
  --red-bg:#fce6e4;
  --green:#2f8a55;
  --green-bg:#e3f3e8;
  --blue:#3f7fc4;
  --blue-bg:#e6f0fb;
}
*{box-sizing:border-box;margin:0;padding:0}
html,body{width:1200px;height:955px;overflow:hidden}
body{font-family:"Inter",sans-serif;background:var(--bg);color:var(--text);position:relative}
.sidebar{position:absolute;left:0;top:0;width:209px;height:955px;background:var(--surface);border-right:1px solid var(--border)}
.brand{height:52px;border-bottom:1px solid var(--border);display:flex;align-items:center;padding-left:16px;gap:10px}
.brand-mark{width:33px;height:33px;border-radius:7px;background:var(--brand)}
.brand-name{font-size:15px;font-weight:600}
.nav{padding:14px 10px 0}
.nav-item{display:flex;align-items:center;gap:12px;height:36px;padding-left:10px;margin-bottom:6.6px;border-radius:6px;font-size:12.3px;color:#3a3d3b}
.nav-item svg{width:15px;height:15px;stroke:currentColor;fill:none;stroke-width:1.7;stroke-linecap:round;stroke-linejoin:round}
.nav-item.active{background:var(--brand);color:#fff;font-weight:500}
.sidebar-foot{position:absolute;left:0;right:0;top:813px;border-top:1px solid var(--border);padding:12px 10px 0}
.theme-toggle{display:flex;align-items:center;gap:12px;height:26px;padding-left:10px;font-size:12.3px;color:#3a3d3b}
.theme-toggle svg{width:15px;height:15px;stroke:currentColor;fill:none;stroke-width:1.7}
.user-card{margin-top:9px;height:80px;border:1px solid var(--border);border-radius:7px;background:#f7f6f3;padding:11px 10px}
.user-row{display:flex;gap:8px;align-items:center}
.avatar{width:26px;height:26px;border-radius:50%;background:var(--brand);color:#fff;font-size:9.5px;font-weight:600;display:flex;align-items:center;justify-content:center}
.user-name{font-size:11.5px;font-weight:500}
.user-mail{font-size:9.8px;color:var(--text-faint)}
.logout{display:flex;align-items:center;gap:7px;margin-top:9px;padding-left:7px;font-size:10.3px;color:#3a3d3b}
.logout svg{width:12px;height:12px;stroke:currentColor;fill:none;stroke-width:1.7}
.main{position:absolute;left:236px;top:0;width:937px}
.page-title{margin-top:27px;font-size:33px;font-weight:500;letter-spacing:-.5px;line-height:40px}
.page-intro{margin-top:5px;font-size:13.1px;line-height:19.7px;color:var(--text-muted)}
.filter-bar{margin-top:16px;height:58px;background:var(--surface);border:1px solid var(--border);border-radius:10px;display:flex;align-items:center;padding-left:14px}
.filter-label{display:flex;align-items:center;gap:6px;font-size:12px;color:var(--text-muted);width:61px}
.filter-label svg{width:13px;height:13px;stroke:currentColor;fill:none;stroke-width:1.6;stroke-linejoin:round}
.search{width:366px;height:30px;border:1px solid #dedcd6;border-radius:6px;display:flex;align-items:center;gap:8px;padding-left:10px;font-size:11.5px;color:var(--text-faint)}
.search svg{width:13px;height:13px;stroke:currentColor;fill:none;stroke-width:1.7}
.select{margin-left:14px;width:126px;height:30px;border:1px solid #dedcd6;border-radius:6px}
.log-card{margin-top:21px;background:var(--surface);border:1px solid var(--border);border-radius:10px;overflow:hidden}
table{width:937px;border-collapse:collapse;table-layout:fixed}
th{height:33px;text-align:left;font-size:9.5px;font-weight:500;letter-spacing:.9px;color:var(--text-faint);border-bottom:1px solid var(--border)}
td{height:51.6px;font-size:11.5px;border-bottom:1px solid var(--border);vertical-align:middle}
tbody tr:nth-child(even){background:var(--row-alt)}
.col-toggle{width:53px;padding-left:18px}
.col-toggle svg{width:10px;height:10px;stroke:var(--text-faint);fill:none;stroke-width:1.6}
.col-time{width:161px;color:#4b4f4c}
.col-sender{width:188px}
.col-subject{width:283px}
.col-cat{width:100px}
.col-score{width:41px;text-align:right;font-weight:500}
.col-action{padding-left:27px;color:#3a3d3b}
.recipient{display:block;font-size:10px;color:var(--text-faint);margin-top:2px}
.tag{display:inline-block;font-size:9.8px;font-weight:500;padding:3px 8px;border-radius:10px}
.tag-newsletter{background:var(--blue-bg);color:var(--blue)}
.tag-phishing{background:var(--orange-bg);color:var(--orange)}
.tag-accepted{background:var(--green-bg);color:var(--green)}
.tag-spam{background:var(--red-bg);color:var(--red)}
.score-mid{color:var(--orange)}
.score-high{color:var(--red)}
.score-low{color:var(--green)}
.table-foot{height:59px;display:flex;align-items:center;padding:0 13px;font-size:12px;color:var(--text-muted)}
.pager{margin-left:auto;display:flex;align-items:center;gap:16px}
.pager-btn{height:28px;padding:0 11px;border:1px solid #dedcd6;border-radius:6px;display:flex;align-items:center;color:#3a3d3b;background:#fff}
</style>
</head>
<body>
<aside class="sidebar">
  <div class="brand"><span class="brand-mark"></span><span class="brand-name">Mailbrook</span></div>
  <nav class="nav">
    <div class="nav-item"><svg viewBox="0 0 24 24"><rect x="3" y="3" width="7" height="9" rx="1"/><rect x="14" y="3" width="7" height="5" rx="1"/><rect x="14" y="12" width="7" height="9" rx="1"/><rect x="3" y="16" width="7" height="5" rx="1"/></svg>Dashboard</div>
    <div class="nav-item active"><svg viewBox="0 0 24 24"><rect x="2" y="4" width="20" height="16" rx="2"/><path d="M2 6l10 7 10-7"/></svg>Mail-Log</div>
    <div class="nav-item"><svg viewBox="0 0 24 24"><path d="M22 12h-6l-2 3h-4l-2-3H2"/><path d="M5.5 5h13L22 12v6a2 2 0 0 1-2 2H4a2 2 0 0 1-2-2v-6z"/></svg>Postfächer</div>
    <div class="nav-item"><svg viewBox="0 0 24 24"><path d="M12 22s8-4 8-10V5l-8-3-8 3v7c0 6 8 10 8 10z"/><path d="M9 12l2 2 4-4"/></svg>Allowlist</div>
    <div class="nav-item"><svg viewBox="0 0 24 24"><path d="M12 22s8-4 8-10V5l-8-3-8 3v7c0 6 8 10 8 10z"/><path d="M9.5 9.5l5 5M14.5 9.5l-5 5"/></svg>Blocklist</div>
    <div class="nav-item"><svg viewBox="0 0 24 24"><rect x="3" y="11" width="18" height="11" rx="2"/><path d="M7 11V7a5 5 0 0 1 10 0v4"/></svg>Quarantäne</div>
    <div class="nav-item"><svg viewBox="0 0 24 24"><circle cx="12" cy="12" r="3"/><path d="M12 2v3M12 19v3M4.9 4.9l2.1 2.1M17 17l2.1 2.1M2 12h3M19 12h3M4.9 19.1L7 17M17 7l2.1-2.1"/></svg>Einstellungen</div>
    <div class="nav-item"><svg viewBox="0 0 24 24"><rect x="2" y="5" width="20" height="14" rx="2"/><path d="M2 10h20"/></svg>Abrechnung</div>
  </nav>
  <div class="sidebar-foot">
    <div class="theme-toggle"><svg viewBox="0 0 24 24"><path d="M21 12.8A9 9 0 1 1 11.2 3a7 7 0 0 0 9.8 9.8z"/></svg>Dunkel</div>
    <div class="user-card">
      <div class="user-row"><span class="avatar">JB</span><div><div class="user-name">Jonas Berger</div><div class="user-mail">admin@example.de</div></div></div>
      <div class="logout"><svg viewBox="0 0 24 24"><path d="M9 21H5a2 2 0 0 1-2-2V5a2 2 0 0 1 2-2h4M16 17l5-5-5-5M21 12H9"/></svg>Abmelden</div>
    </div>
  </div>
</aside>

<main class="main">
  <h1 class="page-title">Mail-Log</h1>
  <p class="page-intro">Hier sehen Sie alle eingehenden E-Mails, die Mailbrook verarbeitet hat. Sie können nach Aktion und Kategorie filtern, um z.B. nur abgelehnte oder als Spam erkannte Nachrichten einzusehen.</p>

  <section class="filter-bar">
    <div class="filter-label"><svg viewBox="0 0 24 24"><path d="M3 4h18l-7 8v7l-4 2v-9z"/></svg>Filter</div>
    <div class="search"><svg viewBox="0 0 24 24"><circle cx="11" cy="11" r="7"/><path d="M20 20l-4-4"/></svg>Suche nach Absender, Betreff...</div>
    <div class="select"></div>
  </section>

  <section class="log-card">
    <table>
      <thead>
        <tr><th class="col-toggle"></th><th class="col-time">ZEIT</th><th class="col-sender">ABSENDER → EMPFÄNGER</th><th class="col-subject">BETREFF</th><th class="col-cat">KATEGORIE</th><th class="col-score">SCORE</th><th class="col-action">AKTION</th></tr>
      </thead>
      <tbody>
        <tr><td class="col-toggle"><svg viewBox="0 0 10 10"><path d="M3.5 2l3 3-3 3"/></svg></td><td class="col-time">15.04.2026, 15:13:58</td><td class="col-sender">newsletter@example.com<span class="recipient">info@firma.de</span></td><td class="col-subject">Wöchentlicher Newsletter - Neue Angebote</td><td class="col-cat"><span class="tag tag-newsletter">Newsletter</span></td><td class="col-score score-mid">25.6</td><td class="col-action">Akzeptiert</td></tr>
        <tr><td class="col-toggle"><svg viewBox="0 0 10 10"><path d="M3.5 2l3 3-3 3"/></svg></td><td class="col-time">15.04.2026, 14:02:05</td><td class="col-sender">support@paywell-secure.ru<span class="recipient">info@firma.de</span></td><td class="col-subject">Urgent: Verify your Paywell account now</td><td class="col-cat"><span class="tag tag-phishing">Phishing</span></td><td class="col-score score-high">89.2</td><td class="col-action">Blockiert</td></tr>
        <tr><td class="col-toggle"><svg viewBox="0 0 10 10"><path d="M3.5 2l3 3-3 3"/></svg></td><td class="col-time">15.04.2026, 13:27:12</td><td class="col-sender">partner@tradepost-mail.com<span class="recipient">kontakt@firma.de</span></td><td class="col-subject">Re: Angebot Zusammenarbeit</td><td class="col-cat"><span class="tag tag-accepted">Akzeptiert</span></td><td class="col-score score-low">2.1</td><td class="col-action">Zugestellt</td></tr>
        <tr><td class="col-toggle"><svg viewBox="0 0 10 10"><path d="M3.5 2l3 3-3 3"/></svg></td><td class="col-time">15.04.2026, 12:45:33</td><td class="col-sender">promo@shop-deals24.net<span class="recipient">info@firma.de</span></td><td class="col-subject">MEGA SALE - 90% Rabatt nur heute!!!</td><td class="col-cat"><span class="tag tag-spam">Spam</span></td><td class="col-score score-high">76.4</td><td class="col-action">Quarantäne</td></tr>
        <tr><td class="col-toggle"><svg viewBox="0 0 10 10"><path d="M3.5 2l3 3-3 3"/></svg></td><td class="col-time">15.04.2026, 11:38:41</td><td class="col-sender">kunde@beispiel.de<span class="recipient">support@firma.de</span></td><td class="col-subject">Frage zu Rechnung #2024-0815</td><td class="col-cat"><span class="tag tag-accepted">Akzeptiert</span></td><td class="col-score score-low">1.3</td><td class="col-action">Zugestellt</td></tr>
        <tr><td class="col-toggle"><svg viewBox="0 0 10 10"><path d="M3.5 2l3 3-3 3"/></svg></td><td class="col-time">15.04.2026, 10:15:22</td><td class="col-sender">noreply@shopora-verify.tk<span class="recipient">admin@firma.de</span></td><td class="col-subject">Your Shopora order has been suspended</td><td class="col-cat"><span class="tag tag-phishing">Phishing</span></td><td class="col-score score-high">92.7</td><td class="col-action">Blockiert</td></tr>
      </tbody>
    </table>
    <div class="table-foot">
      Zeige 6 von 6 Einträgen
      <div class="pager"><span class="pager-btn">Zurück</span><span>Seite 1</span><span class="pager-btn">Weiter</span></div>
    </div>
  </section>
</main>
</body>
</html>
```